Vel Tor Concrete Post Card Design Project

Hello, We are A Concrete Contractor. We specialize in removing and replacing concrete walkways, Patio's, Driveway's, ect., that are a trip hazard. We work a lot in Apartment complexes and Business Complexes where the trees have grown big and the roots from the trees lift up the concrete.
I would like someone to design a postcard (Two Sided) so I can send it out and market potential property manager customers. I would like to use our company logo on this card. Please see the snap vault link below. Here are some things I would like the card to have on it.

1.Removal and Replacement of Concrete Sidewalks, Driveways, Parking Lots, Curb and Gutter.

2. ADA Compliant.

3. Repair of concrete tripping hazards and
root-damaged sidewalks.

4. Vel Tor Concrete brings your sidewalks in compliance with the Americans With Disabilities Act (ADA).

5. Property Management:

We cater to the needs of Property Mangement Companies, HOA, Apartment Complexes, Business Parks, Senior Living Complexes, Government Buildings and Shopping Centers.

6. Free Estimates
7. Contractors license number under our logo. It is:
RBQC #318907
8. Our phone numbers:530-842-1964 and 530-729-6350.

Card should be two sided 9" by 6"

Thank You
Updates

This website would not let me upload my logo so please click on the link below to get it.

 

http://img4471.snapvaultpix.net/albums/k302/Jvelt42/VelTorConcreteLogo-2012-PROOF-2.jpg

Thank You

Reason: Hello, I have a lot of great designs. I have had a busy week and I am just now sitting down to ask for the changes I would like. Once I recieve all of the designs back with the changes I requested I would like to get the opinions of my coworkers and friends before selecting the design. I am asking for the deadline to be extended by 4 days. Thank You so much, Janice Vel Tor

Target Market(s)

Property Managers

Industry/Entity Type

Concrete

Requirements
Must have
• Our logo

```html
<!DOCTYPE html>
<html lang="en">
<head>
<meta charset="utf-8">
<title>Vel Tor Concrete – Trip Hazard Repair Postcard</title>
<link href="https://fonts.googleapis.com/css2?family=Tinos:wght@400;700&family=Chewy&family=Roboto+Condensed:wght@700&display=swap" rel="stylesheet">
<style>
  :root {
    --page-bg: #e9e9e9;
    --concrete-light: #d4d4d4;
    --concrete-mid: #b9b9b9;
    --concrete-dark: #9e9e9e;
    --brand-red: #d3141b;
    --deep-red: #a50d12;
    --maroon: #7a1a2a;
    --white: #ffffff;
    --ink: #1a1a1a;
    --photo-green: #5f9443;
    --photo-stone: #b8afa3;
  }
  * { box-sizing: border-box; margin: 0; padding: 0; }
  html, body { width: 1200px; height: 900px; overflow: hidden; }
  body { background: var(--page-bg); position: relative; }

  .postcard {
    position: absolute; left: 30px; top: 70px;
    width: 1140px; height: 760px; overflow: hidden;
    background:
      radial-gradient(ellipse at 30% 35%, var(--concrete-light) 0%, transparent 60%),
      linear-gradient(100deg, var(--concrete-mid) 0%, var(--concrete-light) 45%, var(--concrete-dark) 100%);
    box-shadow: 0 10px 30px rgba(0,0,0,.25);
  }

  .photo { position: absolute; top: 470px; height: 290px; }
  .photo--lawn-walk { left: 0; width: 354px; background: var(--photo-green); }
  .photo--pour { left: 354px; width: 498px; background: var(--photo-stone); }
  .photo--new-walk { left: 852px; width: 288px; background: var(--photo-green); }

  .swoosh { position: absolute; left: 0; top: 0; width: 1140px; height: 760px; }

  .brand {
    position: absolute; left: 38px; top: 78px; width: 240px;
    display: flex; align-items: center; gap: 10px;
    font-family: "Tinos", serif; font-weight: 700; font-size: 30px; line-height: 1.05;
    color: var(--brand-red);
  }
  .brand__dot { flex: none; width: 22px; height: 22px; border-radius: 50%; background: var(--brand-red); }

  .services {
    position: absolute; left: 40px; top: 215px; list-style: none;
    font-family: "Tinos", serif; font-size: 21px; line-height: 36px;
    color: var(--white); text-shadow: 1px 1px 2px rgba(0,0,0,.85);
  }

  .headline {
    position: absolute; left: 258px; top: 18px; width: 860px; text-align: center;
    font-family: "Tinos", serif; font-weight: 700; font-size: 29px; letter-spacing: .5px;
    color: var(--brand-red); text-transform: uppercase;
    text-shadow: -2px 0 var(--white), 2px 0 var(--white), 0 -2px var(--white), 0 2px var(--white),
                 3px 3px 4px rgba(0,0,0,.6);
  }

  .highlights {
    position: absolute; left: 325px; top: 78px; width: 800px; list-style: none;
    font-family: "Tinos", serif; font-weight: 700; font-size: 21.5px; line-height: 36px;
    color: var(--white); text-shadow: 1px 1px 2px rgba(0,0,0,.9);
  }
  .highlights li { position: relative; padding-left: 22px; margin-bottom: 14px; }
  .highlights li::before {
    content: ""; position: absolute; left: 0; top: 11px; width: 13px; height: 13px;
    border-radius: 50%; background: var(--brand-red); box-shadow: 0 0 0 1.5px var(--white);
  }

  .seal { position: absolute; left: 890px; top: 380px; width: 210px; height: 210px; }

  .call-line {
    position: absolute; left: 30px; top: 688px; white-space: nowrap;
    font-family: "Chewy", cursive; font-size: 40px; color: var(--white);
    text-shadow: -2px 0 var(--ink), 2px 0 var(--ink), 0 -2px var(--ink), 0 2px var(--ink), 2px 3px 3px rgba(0,0,0,.6);
  }
</style>
</head>
<body>
  <article class="postcard">
    <div class="photo photo--lawn-walk" role="img" aria-label="Photo of a curving sidewalk beside green lawn"></div>
    <div class="photo photo--pour" role="img" aria-label="Photo of a worker spreading fresh concrete over rebar"></div>
    <div class="photo photo--new-walk" role="img" aria-label="Photo of a new straight sidewalk between lawns"></div>

    <svg class="swoosh" viewBox="0 0 1140 760" aria-hidden="true">
      <defs>
        <linearGradient id="concreteFill" x1="0" y1="0" x2="1" y2="0">
          <stop offset="0" stop-color="#c0c0c0"/>
          <stop offset=".5" stop-color="#cfcfcf"/>
          <stop offset="1" stop-color="#a6a6a6"/>
        </linearGradient>
      </defs>
      <path d="M0 0 H1140 V500 C950 470 820 490 700 520 C520 565 300 545 0 490 Z" fill="url(#concreteFill)"/>
      <path d="M0 425 C220 520 520 545 760 505 C900 482 1030 468 1140 470 V500 C950 478 820 500 700 525 C520 560 250 545 0 490 Z" fill="var(--brand-red)"/>
      <path d="M0 458 C180 560 380 600 640 520 C820 465 980 470 1140 505" fill="none" stroke="var(--maroon)" stroke-width="6"/>
    </svg>

    <div class="brand"><span class="brand__dot"></span><span>Vel Tor Concrete</span></div>

    <ul class="services">
      <li>Removal &amp; Replacement:</li>
      <li>- Concrete Sidewalks</li>
      <li>- Driveways</li>
      <li>- Parking Lots</li>
      <li>- Curb and Gutters</li>
      <li>- ADA Compliant</li>
    </ul>

    <h1 class="headline">Concrete Trip Hazard Repair and Removal</h1>

    <ul class="highlights">
      <li>Vel Tor Concrete brings your sidewalks in compliance with<br>the Americans With Disabilities Act (ADA).</li>
      <li>Concrete Grinding:<br>Repair of tripping hazard removal, root-damaged sidewalks.</li>
      <li>Property Management:<br>We cater to the needs of Property Mangement Companies, HOA,<br>Apartment Complexes, Business Parks, Senior Living Complex,<br>Government Buildings and Shopping Centers,<br>concrete trip hazard repair and removal,<br>sidewalk concrete repair</li>
    </ul>

    <svg class="seal" viewBox="0 0 200 200" aria-label="24 Hr Service">
      <g fill="var(--deep-red)">
        <rect x="30" y="30" width="140" height="140"/>
        <rect x="30" y="30" width="140" height="140" transform="rotate(15 100 100)"/>
        <rect x="30" y="30" width="140" height="140" transform="rotate(30 100 100)"/>
        <rect x="30" y="30" width="140" height="140" transform="rotate(45 100 100)"/>
        <rect x="30" y="30" width="140" height="140" transform="rotate(60 100 100)"/>
        <rect x="30" y="30" width="140" height="140" transform="rotate(75 100 100)"/>
      </g>
      <circle cx="100" cy="100" r="80" fill="var(--white)"/>
      <circle cx="100" cy="100" r="74" fill="var(--brand-red)"/>
      <g transform="rotate(18 100 100)" font-family="Roboto Condensed, sans-serif" font-weight="700" fill="var(--white)" text-anchor="middle">
        <text x="100" y="94" font-size="34">24 Hr</text>
        <text x="100" y="132" font-size="30">Service</text>
      </g>
    </svg>

    <p class="call-line">Call us now: 530-842-1964 or 530-729-6350</p>
  </article>
</body>
</html>
```